Breakthrough Sports Drink Needs a Label Design

Using the logo provided, we need a label design for a new sports drink company called 'Vorna'. We have developed a clear and light, protein-infused beverage for elite athletes.

We would like to label to use a similar color scheme as the logo provided. It needs to portray a refreshing, healthy feel but also needs to reflect the functional aspects of the drink.

The label needs to clearly include the phrases: "18 grams of protein", "For the Elite Athlete" and " "2:1 ratio of carbs to protein "

Target Market(s)

College Athletes

Industry/Entity Type

It Company

Requirements
Must have
• Should be based on the logo provided and include the phrases:
• 18g of Protein
• For The Elite Athlete
• 2:1 Ratio of Carbs to Protein

```html
<!DOCTYPE html>
<html lang="en">
<head>
<meta charset="utf-8">
<title>Vorna Athletic Recovery – Label</title>
<link rel="stylesheet" href="https://fonts.googleapis.com/css2?family=Open+Sans:wght@600;700;800&display=swap">
<style>
  :root {
    --page-bg: #f3f5f7;
    --label-bg: #eceef0;
    --band-light: #d6e6f5;
    --band-mid: #bcd8f1;
    --brand-gray: #6a7076;
    --accent-blue: #2b8ad6;
    --badge-top: #7cbcf0;
    --badge-bottom: #2f82d2;
    --badge-rim: #d5dadf;
    --badge-rim-dark: #9aa3ab;
    --badge-text: #f4f8fc;
    --ink-dark: #2d3338;
  }
  * { box-sizing: border-box; margin: 0; padding: 0; }
  html, body {
    width: 1200px;
    height: 1000px;
    overflow: hidden;
    background: var(--page-bg);
    font-family: "Open Sans", Arial, sans-serif;
  }
  .canvas {
    position: relative;
    width: 1200px;
    height: 1000px;
  }
  .label {
    position: absolute;
    left: 320px;
    top: 170px;
    width: 560px;
    height: 660px;
    background: var(--label-bg);
    overflow: hidden;
    box-shadow: 0 10px 30px rgba(40, 60, 80, 0.12);
  }
  .label-bands {
    position: absolute;
    inset: 0;
  }
  .brand-name {
    position: absolute;
    left: 50px;
    top: 30px;
    height: 600px;
    writing-mode: vertical-rl;
    transform: rotate(180deg);
    font-weight: 800;
    font-size: 146px;
    line-height: 150px;
    letter-spacing: 2px;
    color: var(--brand-gray);
    text-align: center;
    white-space: nowrap;
  }
  .product-line {
    position: absolute;
    left: 226px;
    top: 30px;
    height: 600px;
    writing-mode: vertical-rl;
    transform: rotate(180deg);
    font-weight: 700;
    font-size: 48px;
    line-height: 60px;
    color: var(--accent-blue);
    text-align: right;
    letter-spacing: 1px;
    white-space: nowrap;
  }
  .claims {
    position: absolute;
    left: 350px;
    top: 40px;
    width: 160px;
    display: flex;
    flex-direction: column;
    align-items: center;
    gap: 20px;
  }
  .claim-badge {
    width: 128px;
    height: 128px;
    border-radius: 20px;
    padding: 6px;
    background: linear-gradient(160deg, var(--badge-rim), var(--badge-rim-dark) 55%, var(--badge-rim));
  }
  .claim-badge-face {
    width: 100%;
    height: 100%;
    border-radius: 15px;
    background: linear-gradient(180deg, var(--badge-top), var(--badge-bottom));
    display: flex;
    flex-direction: column;
    align-items: center;
    justify-content: center;
    color: var(--badge-text);
    text-align: center;
    text-transform: uppercase;
  }
  .claim-figure {
    font-weight: 800;
    font-size: 54px;
    line-height: 54px;
  }
  .claim-note {
    font-weight: 700;
    font-size: 14px;
    line-height: 16px;
    letter-spacing: 0.5px;
  }
  .claim-words {
    font-weight: 800;
    font-size: 34px;
    line-height: 36px;
  }
  .volume {
    font-weight: 800;
    font-size: 32px;
    line-height: 30px;
    color: var(--ink-dark);
    text-align: center;
  }
  .volume-unit {
    display: block;
    font-size: 22px;
  }
  .tagline {
    font-weight: 700;
    font-size: 15px;
    line-height: 18px;
    letter-spacing: 1px;
    color: var(--accent-blue);
    text-align: center;
    text-transform: uppercase;
  }
</style>
</head>
<body>
<main class="canvas">
  <section class="label" aria-label="Vorna Athletic Recovery bottle label">
    <svg class="label-bands" width="560" height="660" viewBox="0 0 560 660" aria-hidden="true">
      <polygon points="0,300 560,60 560,170 0,420" fill="var(--band-light)"/>
      <polygon points="0,470 560,250 560,330 0,560" fill="var(--band-mid)"/>
      <polygon points="120,660 560,470 560,540 280,660" fill="var(--band-light)"/>
    </svg>

    <h1 class="brand-name">VORNA</h1>
    <p class="product-line">ATHLETIC RECOVERY</p>

    <div class="claims">
      <div class="claim-badge">
        <div class="claim-badge-face">
          <span class="claim-figure">2:1</span>
          <span class="claim-note">Carbs<br>to protein</span>
        </div>
      </div>
      <div class="claim-badge">
        <div class="claim-badge-face">
          <span class="claim-figure">18</span>
          <span class="claim-note">Grams<br>of protein</span>
        </div>
      </div>
      <div class="claim-badge">
        <div class="claim-badge-face">
          <span class="claim-words">NO<br>FATS</span>
        </div>
      </div>
      <p class="volume">500<span class="volume-unit">ML</span></p>
      <p class="tagline">For the Elite<br>Athlete</p>
    </div>
  </section>
</main>
</body>
</html>
```